Design a menu for health restaurant

A health food restaurant in Los Angeles is seeking menu design. Our foods are made from scratch using whole ingredients.
Name: Grubb Larder
Address: 1000 E 60th StLos Angeles, CA 90247
Website: www.GrubbLarder.example
We are looking for a clean and simple menu. Brand colors are white/tan, green and orange.

Please see attached excel with menu items and logo. We do not yet have prices.

Colors
f78f20
9bcb3c
ffffff
fff3d1

Requirements
Must have
• Easy to read.
Trifold menu design (front and back).
VEGAN, VEGETARIAN, GLUTEN FREE, CONTAINS NUTS symbols.
Logo.
Nice to have
• Incorporate brand colors, but still be easy to read.
We would like to use the Belco font (attached) if it works. If not we are open to a similar font that is easy to read.

Please see attached images.
We like the images and headers of OPTION 1. Would like something similar in trifold format.
We like the clean fonts of OPTION 2.

```html
<!DOCTYPE html>
<html lang="en">
<head>
<meta charset="utf-8">
<title>Menu</title>
<link rel="stylesheet" href="https://fonts.googleapis.com/css2?family=Bebas+Neue&family=Montserrat:wght@400;500;700;800&display=swap">
<style>
:root{
  --orange:#f78f20;
  --green:#9bcb3c;
  --white:#ffffff;
  --cream:#fff3d1;
  --ink:#222222;
  --body:#3a3a3a;
  --veg:#4cb06a;
  --gf:#7cc4d8;
  --nut:#5a4632;
}
*{margin:0;padding:0;box-sizing:border-box}
html,body{width:1200px;height:927px;overflow:hidden;background:var(--white)}
.menu{position:relative;width:1200px;height:927px;background:var(--white);font-family:"Montserrat",Arial,sans-serif;color:var(--body)}
.center-bg{position:absolute;left:402px;top:0;width:406px;height:927px;background:var(--cream)}
.divider{position:absolute;top:0;height:927px;border-left:2px dotted var(--green)}
.band{position:absolute;height:60px;overflow:hidden;font-family:"Bebas Neue",Impact,sans-serif;font-size:52px;line-height:52px;color:var(--cream);letter-spacing:1.5px}
.band--orange{background:var(--orange)}
.band--green{background:var(--green)}
.band span{position:absolute;left:46px;top:16px}
.item{position:absolute}
.item h3{display:block;white-space:nowrap;font-weight:800;font-size:16px;line-height:18px;color:var(--ink);letter-spacing:.3px}
.item p{font-size:12.6px;line-height:16.8px;margin-top:1px}
.item p b{font-weight:700;color:var(--ink)}
.item p i{font-style:italic}
.ic{display:inline-block;width:16px;height:16px;vertical-align:-2px;margin-left:1px}
.ic.first{margin-left:5px}
.dotbox{position:absolute;border:2px dotted var(--orange)}
.sub{font-size:12.6px;font-weight:700;color:var(--ink);line-height:16px;white-space:nowrap}
</style>
</head>
<body>
<svg width="0" height="0" style="position:absolute" aria-hidden="true">
  <defs>
    <symbol id="i-vegan" viewBox="0 0 20 20"><circle cx="10" cy="10" r="10" fill="#f78f20"/><path d="M6 5 L10 15 L14 5" fill="none" stroke="#fff" stroke-width="2.4" stroke-linecap="round" stroke-linejoin="round"/></symbol>
    <symbol id="i-gf" viewBox="0 0 20 20"><circle cx="10" cy="10" r="9" fill="#fff" stroke="#7cc4d8" stroke-width="1.8"/><path d="M10 16 V6 M10 9 L7 7 M10 9 L13 7 M10 12 L7 10 M10 12 L13 10" fill="none" stroke="#7cc4d8" stroke-width="1.5" stroke-linecap="round"/></symbol>
    <symbol id="i-nut" viewBox="0 0 20 20"><circle cx="10" cy="10" r="10" fill="#5a4632"/><ellipse cx="10" cy="10" rx="6" ry="4.5" fill="#e9dcc4"/><path d="M6 9 Q10 12 14 9 M7 11 Q10 13 13 11" fill="none" stroke="#5a4632" stroke-width="1"/></symbol>
    <symbol id="i-veg" viewBox="0 0 20 20"><circle cx="10" cy="10" r="10" fill="#4cb06a"/><path d="M5 14 C5 7 10 5 15 5 C15 11 12 15 6 14 Z" fill="#fff"/><path d="M6 14 L12 8" stroke="#4cb06a" stroke-width="1.2"/></symbol>
  </defs>
</svg>

<main class="menu">
  <div class="center-bg"></div>
  <div class="divider" style="left:401px"></div>
  <div class="divider" style="left:807px"></div>

  <!-- Breakfast -->
  <div class="band band--orange" style="left:0;top:0;width:401px"><span>Breakfast</span></div>
  <div class="dotbox" style="left:-4px;top:81px;width:385px;height:96px;border-left:none"></div>
  <div class="item" style="left:42px;top:94px;width:340px">
    <h3>PASTRIES<svg class="ic first"><use href="#i-veg"/></svg></h3>
    <p><b>Croissant</b> <i>(regular, almond, chocolate)</i> 0.00<br><b>Blueberry Muffin</b> 0.00<br><b>Superseed Cookie</b> 0.00</p>
  </div>
  <div class="item" style="left:42px;top:192px;width:340px">
    <h3>PARFAIT<svg class="ic first"><use href="#i-veg"/></svg></h3>
    <p>Fresh strawberries and blueberries on yogurt and muesli and topped with honey drizzle. 0.00</p>
  </div>
  <div class="item" style="left:42px;top:262px;width:340px">
    <h3>AVOCADO SUPER TOAST<svg class="ic first"><use href="#i-vegan"/></svg></h3>
    <p>Avocado Mash, Tomato, Basil, Ground Flax, Hemp Seed, Chickpeas, and Moringa Powder on Whole Wheat Bread. 0.00</p>
  </div>
  <div class="item" style="left:42px;top:348px;width:340px">
    <h3>BREAKFAST SAMMY</h3>
    <p>Your choice of over medium egg or tofu steak with guacamole, tomato, and Larder sauce on an English muffin. 0.00 (Vegan option available)</p>
  </div>
  <div class="item" style="left:42px;top:434px;width:340px">
    <h3>BRUNCH BURGER</h3>
    <p>House seasoned beef burger topped with an over medium egg, red leaf lettuce, tomato, housemade pickles and Larder Sauce on a bun. 0.00</p>
  </div>
  <div class="item" style="left:42px;top:521px;width:340px">
    <h3>AM BURRITO<svg class="ic first"><use href="#i-veg"/></svg></h3>
    <p>Scrambled eggs, onion, red bell pepper, black beans, housemade salsa, yogurt, and pepper jack cheese in a tortilla. 0.00</p>
  </div>

  <!-- Smoothies -->
  <div class="band band--green" style="left:0;top:633px;width:401px"><span>Smoothies</span></div>
  <div class="item" style="left:42px;top:719px;width:345px">
    <h3>GREEN MACHINE SMOOTHIE<svg class="ic first"><use href="#i-vegan"/></svg><svg class="ic"><use href="#i-gf"/></svg><svg class="ic"><use href="#i-nut"/></svg></h3>
    <p>Romaine, spinach, banana, mango, pineapple, flaxmilk, spirulina, almond butter</p>
  </div>
  <div class="item" style="left:42px;top:789px;width:345px">
    <h3>ACAI SMOOTHIE<svg class="ic" style="margin-left:10px"><use href="#i-vegan"/></svg><svg class="ic"><use href="#i-gf"/></svg><svg class="ic"><use href="#i-nut"/></svg></h3>
    <p>Acai, blueberries, banana, pineapple, Macqui berry, flaxmilk, almond butter</p>
  </div>
  <div class="item" style="left:42px;top:858px;width:345px">
    <h3>MANGO SMOOTHIE<svg class="ic" style="margin-left:10px"><use href="#i-vegan"/></svg><svg class="ic"><use href="#i-gf"/></svg></h3>
    <p>Mango, flaxmilk, banan, hemp seeds</p>
  </div>

  <!-- Bowls -->
  <div class="band band--green" style="left:403px;top:0;width:404px"><span style="left:36px">Bowls</span></div>
  <div class="item" style="left:437px;top:83px;width:160px">
    <h3>SOUTHWEST<br>BOWL<svg class="ic first"><use href="#i-gf"/></svg><svg class="ic"><use href="#i-nut"/></svg></h3>
    <p>Your choice of protein with corn, black beans, red onions, almonds and avocado over quinoa with lime hot sauce. 0.00</p>
  </div>
  <div class="item" style="left:437px;top:221px;width:160px">
    <h3>CHIMI BOWL<svg class="ic first"><use href="#i-gf"/></svg></h3>
    <p>Your choice of protein with red bell pepper, mushrooms, zucchini, squash, onion, cherry tomatoes and fresh herb chimichurri on wild and brown rice. 0.00</p>
  </div>
  <div class="item" style="left:437px;top:374px;width:160px">
    <h3>SOBA<br>NOODLE BOWL</h3>
    <p>Your choice of protein with spinach, snow peas, roasted carrots, red bell pepper, cilantro, sesame seeds and ginger lime sauce over soba noodles. 0.00</p>
  </div>
  <div class="item" style="left:619px;top:83px;width:168px">
    <h3>HOLLYWOOD<br>BOWL<svg class="ic first"><use href="#i-gf"/></svg></h3>
    <p>Your choice of protein with broccoli, roasted corn, cherry tomatoes, basil, pepitas, flax seeds and lemon juice on wild and brown rice. 0.00</p>
  </div>
  <div class="item" style="left:619px;top:237px;width:168px">
    <h3>LARDER BOWL<svg class="ic first"><use href="#i-gf"/></svg></h3>
    <p>Your choice of protein with roasted chickpeas and cauliflower, zesty fennel salad and citrus yogurt. 0.00</p>
  </div>
  <div class="item" style="left:619px;top:357px;width:168px">
    <h3>BUDDHA BOWL</h3>
    <p>Your choice of protein with corn, red kale, sweet potatoes, red cabbage, parsley, oregano, hummus, and farro. 0.00</p>
  </div>
  <div class="item" style="left:619px;top:477px;width:168px">
    <h3>CHILI RICE BOWL<svg class="ic first"><use href="#i-gf"/></svg></h3>
    <p>Chicken, onions, bell peppers, jalapeños, black &amp; kidney beans, and tomato over brown rice.</p>
  </div>

  <!-- Soup -->
  <div class="band band--orange" style="left:403px;top:604px;width:404px"><span style="left:36px">Soup</span></div>
  <div class="item" style="left:438px;top:690px;width:330px">
    <h3>CHICKEN NOODLE<svg class="ic first"><use href="#i-gf"/></svg></h3>
    <p>Chicken, egg noodles, root vegetables, oregano &amp; peppercorns.</p>
  </div>
  <div class="item" style="left:438px;top:760px;width:330px">
    <h3>LARDER CHILI<svg class="ic first"><use href="#i-gf"/></svg></h3>
    <p>Chicken, onions, bell peppers, jalapeños, black &amp; kidney beans, and tomato.</p>
  </div>
  <div class="dotbox" style="left:424px;top:820px;width:362px;height:120px;border-bottom:none"></div>
  <div class="item" style="left:438px;top:830px;width:330px">
    <h3>SEASONAL ROTATING</h3>
    <div class="sub">Butternut Squash Soup<svg class="ic first"><use href="#i-vegan"/></svg><svg class="ic"><use href="#i-gf"/></svg></div>
    <p>Butternut squash blended with warm spices, and coconut milk.</p>
  </div>

  <!-- Wraps -->
  <div class="band band--orange" style="left:809px;top:0;width:391px"><span style="left:34px">Wraps</span></div>
  <div class="item" style="left:843px;top:82px;width:335px">
    <h3>RANCHER’S WRAP<svg class="ic first"><use href="#i-veg"/></svg></h3>
    <p>Tomato, red onion, hard boiled egg, avocado, feta cheese, microgreens, romaine, grilled chicken and Ranch dressing in a grilled wrap.</p>
  </div>
  <div class="item" style="left:843px;top:169px;width:335px">
    <h3>VEGAN TUNA WRAP<svg class="ic first"><use href="#i-vegan"/></svg></h3>
    <p>Vegan tuna, romaine, avocado, celery, shallot, and oregano with Herbalicious Sauce in a whole grain wrap.</p>
  </div>
  <div class="item" style="left:843px;top:255px;width:335px">
    <h3>VEGETARIAN WRAP<svg class="ic first"><use href="#i-veg"/></svg></h3>
    <p>Roasted chickpeas, romaine, avocado, red bell pepper, shaved carrots, cucumber, spinach, basil, black beans and feta with lemon-hummus in a sprouted 7-grain wrap.</p>
  </div>

  <!-- Salads -->
  <div class="band band--green" style="left:809px;top:380px;width:391px"><span style="left:37px">Salads</span></div>
  <div class="item" style="left:846px;top:468px;width:335px">
    <h3>AVOCADO, GOLDEN BEET, AND<br>CRANBERRY SALAD<svg class="ic" style="margin-left:10px"><use href="#i-vegan"/></svg><svg class="ic"><use href="#i-gf"/></svg></h3>
    <p>Gold beets, avocado, dried cranberries, watermelon radish, red kale, romaine, mixed greens, and pepitas served with Golden Buddha dressing.</p>
  </div>
  <div class="item" style="left:846px;top:573px;width:335px">
    <h3>BURRATA SALAD<svg class="ic" style="margin-left:12px"><use href="#i-vegan"/></svg><svg class="ic"><use href="#i-gf"/></svg></h3>
    <p>Tomato, melon, shredded basil, balsamic glaze, fresh cracked pepper, and olive oil with burrata.</p>
  </div>
  <div class="item" style="left:846px;top:642px;width:335px">
    <h3>MEDITERRANEAN SALAD<svg class="ic first"><use href="#i-vegan"/></svg><svg class="ic"><use href="#i-gf"/></svg></h3>
    <p>Cucumbers, Kalamata olives, cherry tomatoes, parsley, tricolor quinoa, hard-boiled egg, and hummus on mixed greens, romaine, and red cabbage with lemon-olive oil dressing.</p>
  </div>
  <div class="item" style="left:846px;top:745px;width:335px">
    <h3>VEGAN CHEF SALAD<svg class="ic first"><use href="#i-vegan"/></svg><svg class="ic"><use href="#i-gf"/></svg><svg class="ic"><use href="#i-nut"/></svg></h3>
    <p>Roasted potatoes and carrots, chickpeas, avocado, microgreens and walnuts on mixed greens, romaine, and red kale with vegan ranch.</p>
  </div>
  <div class="item" style="left:846px;top:832px;width:335px">
    <h3>RANCHER’S SALAD<svg class="ic first"><use href="#i-vegan"/></svg><svg class="ic"><use href="#i-gf"/></svg></h3>
    <p>Tomato, red onion, hard boiled egg, avocado, feta cheese, microgreens, and grilled chicken on romaine with Ranch dressing.</p>
  </div>
</main>
</body>
</html>
```